Smart, intuitive SaaS software dashboard design

PactBloom is an innovative modern SaaS (software as a service) solution for contract and meeting management.

What we are looking for is fresh ideas for our dashboard. We do not need web coding or actionable wireframes now – but purely great design ideas from where to continue forward.

How should a modern web software dashboard look like? Fresh, intuitive, easy-to-use, and adaptable for responsive mobile designs. We hope that when the user logs into the service and sees the dashboard, he/she gets a good big picture of the current status of the most important documents of his/hers company.

To get to know the service and see the components, we kindly ask you to register to our service at www.pactbloom-demo.net and to utilize the free trial (30 days) so you can see the existing dashboard live. And also try out how it works. Might help you to get ideas how to improve it.

(The designer we will choose might be offered later on to design some other pages as well (contract view and edit pages, meeting page etc).)

You’ll find additional information in the attachment.

You’ll find more information of the company and the service also at www.pactbloom-demo.net

Target Market(s)

Global

Industry/Entity Type

Business Management

Number of Pages Required

1 page

Font styles to use
Sans Serif

Requirements
Must have
• 1) Clear design idea for us to iterate from, 2) Modern look and feel - elegant & bold at the same time - still with credibility in our target group. And 3) Suitable for dashboard usage - it should it a clear big picture for the user.
• UPDATE:
• Users should see most important things with one glance. Therefore we would like to see AT LEAST these items mentioned below on the first page.
• NOTE: if all these things are visible on the dashboard, the menu list is maybe not needed on the left. (And there might be some icons on the top header with needed settings/inbox features anyway.)
• NOTE2: as explained earlier, the design should be responsive i.e. work without modifications in PC, iPad and mobile (the areas/boxes would just rearrange themselves on top of each other.)
• -First area should be Documents, which would include different document categories: Contracts, Finance & Admin and HR
• -All different types of Meetings could be the next area (upcoming ones clearly visible with date and maybe description, time and location visible also).
• -Reminders and Activity Feed (they might also be together in top of each other, so that Reminder is visible first and Activity feed can be chosen from the tab.)
• -Virtual Datarooms (maybe 1-3 different ones with some analytics for each visible e.g. like usage/visits per day)
• Saved searches in very important list as users can save their most important searches. There are typically many of these, so at least 5 should be visible and then see all button (maybe even more could be visible if they fit on your design)
• My Latest is also important.
• (As explained, Action Required area is NOT needed anymore).
Nice to have
• Surprise us!
Should not have
• Please avoid the boring traditional legacy stuff and the common report dashboards.
• You do not need design a 100% mockup for the techie to continue with. The ideas count.

```html
<!DOCTYPE html>
<html lang="en">
<head>
<meta charset="utf-8">
<title>PactBloom Dashboard</title>
<link href="https://fonts.googleapis.com/css2?family=Open+Sans:wght@400;600;700&display=swap" rel="stylesheet">
<style>
:root{
  --black:#000;
  --side:#2b2b2b;
  --side-dark:#1f1f1f;
  --blue:#2a6cc6;
  --blue-bright:#1b6fd1;
  --link:#1a63c0;
  --bg:#e9e9e9;
  --white:#fff;
  --row:#f1f1f1;
  --ink:#222;
  --muted:#555;
  --pill:#3a3a3a;
  --tab:#d9d9d9;
  --foot:#3a3a3a;
}
*{box-sizing:border-box;margin:0;padding:0}
html,body{width:1200px;height:742px;overflow:hidden}
body{font-family:'Open Sans',sans-serif;background:var(--bg);color:var(--ink);position:relative;font-size:11px}
.abs{position:absolute}
.topbar{position:absolute;left:0;top:0;width:1200px;height:54px;background:var(--black)}
.brand{position:absolute;left:14px;top:12px;display:flex;align-items:center;gap:8px;color:#fff;font-size:17px;letter-spacing:1px;font-weight:400}
.brand-dot{width:24px;height:24px;border-radius:50%;background:var(--blue-bright)}
.search{position:absolute;left:380px;top:11px;width:548px;height:32px;background:#fff;border-radius:16px}
.search svg{position:absolute;left:10px;top:8px}
.search .scope{position:absolute;right:20px;top:7px;color:var(--link);font-size:13px}
.tools{position:absolute;left:976px;top:17px;display:flex;gap:12px}
.tools .ic{position:relative}
.badge{position:absolute;right:-7px;top:-6px;width:12px;height:12px;border-radius:50%;background:var(--blue-bright);color:#fff;font-size:8px;text-align:center;line-height:12px}
.user{position:absolute;left:1065px;top:18px;display:flex;align-items:center;gap:6px;color:#fff;font-size:11px}
.user .av{width:20px;height:20px;border-radius:50%;background:#b9a28f}
.side{position:absolute;left:0;top:54px;width:203px;height:650px;background:var(--side);color:#ddd}
.welcome{position:absolute;left:12px;top:19px;display:flex;gap:12px;align-items:center}
.welcome .av{width:45px;height:45px;border-radius:50%;background:#c9b4a2;border:3px solid #fff}
.welcome p{color:#fff;font-size:14px;line-height:18px;font-weight:600}
.status{position:absolute;left:14px;top:73px;font-size:9.5px;color:#bbb;display:flex;gap:8px;align-items:center}
.status i{width:13px;height:13px;border-radius:50%;background:var(--blue-bright)}
.menu{position:absolute;left:0;top:105px;width:203px;list-style:none}
.menu li{height:30.5px;display:flex;align-items:center;padding:0 12px;font-size:11px;position:relative}
.menu li svg{margin-right:8px}
.menu li .pl{position:absolute;right:20px;font-size:13px}
.menu .open{background:var(--side-dark);border-top:1px solid var(--blue);height:34px}
.sub{position:absolute;left:0;width:203px;list-style:none}
.sub li{height:23px;font-size:11px;padding-left:20px;display:flex;align-items:center}
.sub li:before{content:"›";margin-right:9px;font-size:13px}
.saved-head{position:absolute;left:0;top:398px;width:203px;height:35px;background:var(--side-dark);display:flex;align-items:center;padding:0 12px;font-size:11px;color:#fff}
.panel{position:absolute;background:#fff}
.phead{height:40px;display:flex;align-items:center;padding:0 14px;color:#fff;font-weight:700;font-size:13px;letter-spacing:.3px;gap:10px}
.blue{background:var(--blue)}
.dark{background:var(--black)}
.doc{left:223px;top:109px;width:256px;height:547px}
.drow{position:absolute;left:3px;width:250px;height:96px}
.drow.alt{background:var(--row)}
.drow .icon{position:absolute;left:13px;top:25px}
.drow h3{position:absolute;left:70px;top:10px;font-size:14px;font-weight:600;letter-spacing:.4px}
.stats{position:absolute;left:70px;top:32px;display:flex}
.stats div{padding:0 7px;border-left:1px solid #ccc;text-align:center;font-size:11px;color:#444}
.stats div:first-child{border:0;padding-left:0}
.stats b{display:block;color:var(--link);font-size:13px;font-weight:400}
.pills{position:absolute;left:73px;top:73px;display:flex;gap:9px}
.pill{background:var(--pill);color:#fff;font-size:9.5px;font-weight:600;border-radius:8px;padding:1px 10px}
.seeall{position:absolute;left:0;bottom:0;width:256px;height:38px;background:#c9c9c9;font-weight:700;font-size:11.5px;text-align:center;line-height:38px;border-bottom:3px solid #fff}
.meet{left:507px;top:110px;width:342px;height:339px}
.meet .btns{margin-left:auto;display:flex;gap:8px}
.meet .btns span{background:#fff;color:#222;font-weight:400;font-size:10px;padding:4px 9px}
.mitem{position:absolute;left:0;width:342px}
.mitem.alt{background:var(--row)}
.date{position:absolute;left:13px;top:15px;width:57px;height:64px}
.date b{display:block;height:42px;background:var(--blue);color:#fff;font-size:29px;font-weight:600;text-align:center;line-height:42px}
.date span{display:block;height:22px;background:#111;color:#fff;font-size:10.5px;text-align:center;line-height:22px}
.mitem h4{position:absolute;left:85px;top:14px;font-size:13.5px;font-weight:600;letter-spacing:.3px}
.mitem p{position:absolute;left:85px;top:34px;width:240px;font-size:10.5px;line-height:15px;color:#444}
.meta{position:absolute;left:85px;top:68px;font-size:10px;color:var(--link);display:flex;gap:6px;align-items:center}
.vdr{left:507px;top:472px;width:342px;height:182px}
.vcol{position:absolute;text-align:center}
.vcol svg{display:block;margin:0 auto}
.vsep{position:absolute;top:50px;width:1px;height:122px;background:#ddd}
.rem{left:876px;top:110px;width:286px;height:268px}
.tabs{display:flex;height:36px}
.tab{display:flex;align-items:center;gap:8px;padding:0 9px;font-size:13px}
.tab.on{border-top:3px solid var(--blue);width:130px;background:#fff}
.tab.off{background:var(--tab);flex:1}
.month{position:absolute;top:60px;left:0;width:286px;text-align:center;font-size:12.5px}
.cal{position:absolute;left:8px;top:88px;width:270px;border-collapse:collapse}
.cal td,.cal th{width:38.5px;height:25px;text-align:center;font-size:10px}
.cal th{font-weight:700;font-size:9px}
.cal .fd{color:#ccc}
.cal .sel span{display:inline-block;width:29px;height:22px;line-height:22px;background:var(--blue-bright);color:#fff;font-size:11px}
.tip{position:absolute;left:91px;top:168px;width:137px;height:48px;background:#555;color:#fff;font-size:9px;line-height:12px;padding:5px 8px}
.saved{left:876px;top:426px;width:286px;height:228px}
.stable{position:absolute;left:10px;top:52px;width:266px;border-collapse:collapse}
.stable th{text-align:left;font-size:10.5px;font-weight:600;height:26px;border-bottom:1px solid #ccc;padding-left:2px}
.stable td{height:23px;font-size:10.5px;border-bottom:1px solid #ddd;padding-left:5px;color:#333}
.stable .act{color:var(--link)}
.stable .act i{color:#aaa;font-style:normal}
.foot{position:absolute;left:0;top:704px;width:1200px;height:38px;background:var(--foot);color:#aaa;font-size:11px}
.foot .c{position:absolute;left:246px;top:12px}
.foot .l{position:absolute;right:68px;top:12px}
</style>
</head>
<body>

<header class="topbar">
  <div class="brand"><span class="brand-dot"></span>PactBloom</div>
  <div class="search">
    <svg width="16" height="16" viewBox="0 0 16 16"><circle cx="6.5" cy="6.5" r="5" fill="none" stroke="#222" stroke-width="2"/><path d="M10 10l5 5" stroke="#222" stroke-width="2"/></svg>
    <span class="scope">Contracts ⌄</span>
  </div>
  <div class="tools">
    <span class="ic"><svg width="18" height="14" viewBox="0 0 18 14"><rect x="1" y="1" width="16" height="12" fill="#fff"/><path d="M1 1l8 7 8-7" fill="none" stroke="#000" stroke-width="1.5"/></svg><span class="badge">2</span></span>
    <span class="ic"><svg width="16" height="16" viewBox="0 0 16 16"><circle cx="8" cy="8" r="5.5" fill="none" stroke="#fff" stroke-width="3" stroke-dasharray="3 1.3"/><circle cx="8" cy="8" r="2.5" fill="#fff"/></svg><span class="badge">3</span></span>
  </div>
  <div class="user"><span class="av" role="img" aria-label="User profile photo"></span>John Doe ⌄</div>
</header>

<aside class="side">
  <div class="welcome"><span class="av" role="img" aria-label="User profile photo"></span><p>Welcome,<br>John Doe</p></div>
  <div class="status">STATUS <i></i> ONLINE</div>
  <ul class="menu">
    <li><svg width="14" height="12" viewBox="0 0 14 12"><path d="M7 0l7 6h-2v6H9V8H5v4H2V6H0z" fill="#ddd"/></svg>HOME<span class="pl">+</span></li>
    <li><svg width="12" height="14" viewBox="0 0 12 14"><rect x="1" y="1" width="10" height="12" fill="none" stroke="#ddd"/><path d="M3 5h6M3 8h6M3 11h4" stroke="#ddd"/></svg>CONTRACTS<span class="pl">+</span></li>
    <li><svg width="12" height="14" viewBox="0 0 12 14"><circle cx="6" cy="4" r="3.5" fill="#ddd"/><path d="M0 14c0-5 12-5 12 0z" fill="#ddd"/></svg>FINANCE<span class="pl">+</span></li>
    <li><svg width="16" height="12" viewBox="0 0 16 12"><circle cx="8" cy="3" r="3" fill="#ddd"/><circle cx="3" cy="4" r="2" fill="#ddd"/><circle cx="13" cy="4" r="2" fill="#ddd"/><path d="M2 12c0-6 12-6 12 0z" fill="#ddd"/></svg>HR &amp; ADMIN<span class="pl">+</span></li>
    <li><svg width="14" height="14" viewBox="0 0 14 14"><circle cx="7" cy="7" r="6" fill="none" stroke="#ddd" stroke-width="1.4"/><text x="7" y="10" font-size="8" text-anchor="middle" fill="#ddd" font-family="Open Sans,sans-serif">R</text></svg>COMPANY REGISTER<span class="pl">+</span></li>
    <li><svg width="14" height="14" viewBox="0 0 14 14"><ellipse cx="7" cy="3" rx="6" ry="2.5" fill="#ddd"/><path d="M1 6c0 3 12 3 12 0M1 9c0 3 12 3 12 0" fill="none" stroke="#ddd" stroke-width="2"/></svg>VIRTUAL DATA ROOMS<span class="pl">+</span></li>
    <li class="open"><svg width="18" height="14" viewBox="0 0 18 14"><rect x="6" y="0" width="6" height="4" fill="#fff"/><rect x="0" y="10" width="5" height="4" fill="#fff"/><rect x="6.5" y="10" width="5" height="4" fill="#fff"/><rect x="13" y="10" width="5" height="4" fill="#fff"/><path d="M9 4v6M2.5 10V7h13v3" fill="none" stroke="#fff"/></svg><span style="color:#fff">MEETINGS</span><span class="pl">⌄</span></li>
  </ul>
  <ul class="sub" style="top:336px">
    <li>Board Meetings</li>
    <li>Shareholders Meetings</li>
  </ul>
  <div class="saved-head"><svg width="14" height="14" viewBox="0 0 16 16" style="margin-right:10px"><circle cx="6.5" cy="6.5" r="5" fill="none" stroke="#fff" stroke-width="2"/><path d="M10 10l5 5" stroke="#fff" stroke-width="2"/></svg>SAVED SEARCHES<span style="margin-left:auto;margin-right:6px">⌄</span></div>
  <ul class="sub" style="top:445px">
    <li>All sales agreements</li>
    <li>Key agreements 2015</li>
    <li>Co-op agreements 2015</li>
    <li>Purchase agreement</li>
    <li>My contacts</li>
    <li>Sales contacts/marketing</li>
  </ul>
</aside>

<section class="panel doc">
  <div class="phead blue"><svg width="13" height="11" viewBox="0 0 13 11"><path d="M0 1h13M0 5.5h13M0 10h13" stroke="#fff" stroke-width="2"/></svg>DOCUMENT</div>
  <div class="drow" style="top:43px">
    <svg class="icon" width="48" height="40" viewBox="0 0 48 40"><rect x="2" y="6" width="32" height="30" rx="3" fill="none" stroke="#222" stroke-width="3"/><path d="M14 28l4-9 20-18 5 5-20 18z" fill="#222"/></svg>
    <h3>CONTRACTS</h3>
    <div class="stats"><div>Total<b>#154</b></div><div>Stattred<b>42</b></div><div>In Progress<b>07</b></div></div>
    <div class="pills"><span class="pill">Folder View</span><span class="pill">Search</span></div>
  </div>
  <div class="drow alt" style="top:152px">
    <svg class="icon" width="44" height="34" viewBox="0 0 44 34"><rect x="1" y="3" width="42" height="28" fill="#222"/><rect x="6" y="8" width="32" height="18" fill="#fff"/><circle cx="22" cy="17" r="7" fill="#222"/><text x="22" y="21" font-size="10" fill="#fff" text-anchor="middle" font-family="Open Sans,sans-serif" font-weight="700">1</text></svg>
    <h3>FINANCE</h3>
    <div class="stats"><div>Total<b>#154</b></div><div>Stattred<b>42</b></div><div>In Progress<b>07</b></div></div>
    <div class="pills"><span class="pill">Folder View</span><span class="pill">Search</span></div>
  </div>
  <div class="drow" style="top:253px">
    <svg class="icon" width="48" height="38" viewBox="0 0 48 38"><circle cx="17" cy="9" r="8" fill="#222"/><path d="M0 37c0-16 30-16 30 0z" fill="#222"/><path d="M38 16v18M29 25h18" stroke="#222" stroke-width="5"/></svg>
    <h3>ADMIN</h3>
    <div class="stats"><div>Total<b>#154</b></div><div>Stattred<b>42</b></div><div>In Progress<b>07</b></div></div>
    <div class="pills"><span class="pill">Folder View</span><span class="pill">Search</span></div>
  </div>
  <div class="drow alt" style="top:354px">
    <svg class="icon" width="46" height="42" viewBox="0 0 46 42"><circle cx="10" cy="8" r="6" fill="#222"/><circle cx="36" cy="8" r="6" fill="#222"/><circle cx="23" cy="14" r="7" fill="#222"/><path d="M0 28c0-12 20-12 20 0zM26 28c0-12 20-12 20 0z" fill="#222"/><path d="M10 42c0-18 26-18 26 0z" fill="#222"/></svg>
    <h3>HR &amp; ADMIN</h3>
    <div class="stats"><div>Total<b>#154</b></div><div>Stattred<b>42</b></div><div>In Progress<b>07</b></div></div>
    <div class="pills"><span class="pill">Folder View</span><span class="pill">Search</span></div>
  </div>
  <div class="seeall">See All</div>
</section>

<section class="panel meet">
  <div class="phead dark"><svg width="18" height="14" viewBox="0 0 18 14"><rect x="6" y="0" width="6" height="4" fill="#fff"/><rect x="0" y="10" width="5" height="4" fill="#fff"/><rect x="6.5" y="10" width="5" height="4" fill="#fff"/><rect x="13" y="10" width="5" height="4" fill="#fff"/><path d="M9 4v6M2.5 10V7h13v3" fill="none" stroke="#fff"/></svg>MEETING<div class="btns"><span>Add</span><span>See All</span></div></div>
  <div class="mitem" style="top:40px;height:104px">
    <div class="date"><b>17</b><span>MAY 2016</span></div>
    <h4>Board Meetings</h4>
    <p>Curabitur convallis lacus urna, eu mauris luctus nec libero dui, porttitor amet.</p>
    <div class="meta">▦ July 21, 2015 &nbsp; <svg width="8" height="10" viewBox="0 0 8 10"><path d="M4 10L1 5a3.5 3.5 0 1 1 6 0z" fill="#555"/></svg> 02150 Rivermark, Nordland</div>
  </div>
  <div class="mitem alt" style="top:144px;height:94px">
    <div class="date" style="top:11px"><b>26</b><span>MAY 2016</span></div>
    <h4 style="top:11px">Shareholders' Meetings</h4>
    <p style="top:31px">Curabitur eu ultrices mauris luctus nec libero dui, porttitor sit amet.</p>
    <div class="meta" style="top:65px">▦ July 21, 2015 &nbsp; <svg width="8" height="10" viewBox="0 0 8 10"><path d="M4 10L1 5a3.5 3.5 0 1 1 6 0z" fill="#555"/></svg> 02150 Rivermark, Nordland</div>
  </div>
  <div class="mitem" style="top:238px;height:100px">
    <div class="date" style="top:10px"><b>12</b><span>MAY 2016</span></div>
    <h4 style="top:10px">Other Meetings</h4>
    <p style="top:30px">Curabitur urna, eu ultrices mauris luctus nec libero dui, porttitor sit amet.</p>
    <div class="meta" style="top:64px">▦ July 21, 2015 &nbsp; <svg width="8" height="10" viewBox="0 0 8 10"><path d="M4 10L1 5a3.5 3.5 0 1 1 6 0z" fill="#555"/></svg> 02150 Rivermark, Nordland</div>
  </div>
</section>

<section class="panel vdr">
  <div class="phead blue"><svg width="16" height="16" viewBox="0 0 14 14"><ellipse cx="7" cy="3" rx="6" ry="2.5" fill="#fff"/><path d="M1 6c0 3 12 3 12 0M1 9c0 3 12 3 12 0" fill="none" stroke="#fff" stroke-width="2"/></svg>VIRTUAL DATA ROOM</div>
  <div class="vcol" style="left:4px;width:116px;top:57px">
    <svg width="58" height="58" viewBox="0 0 60 60"><circle cx="30" cy="30" r="26" fill="none" stroke="#ddd" stroke-width="4"/><path d="M30 4a26 26 0 0 1 12 49" fill="none" stroke="#333" stroke-width="5"/><text x="30" y="28" text-anchor="middle" font-size="10" font-weight="600" font-family="Open Sans,sans-serif">50</text><text x="30" y="42" text-anchor="middle" font-size="14" font-weight="700" font-family="Open Sans,sans-serif">GB</text></svg>
    <div style="font-size:10px;font-weight:700;margin-top:6px">USAGES</div>
    <div style="font-size:8px;color:#666">You must complete Issues.</div>
    <div style="display:flex;gap:8px;justify-content:center;margin-top:5px"><span style="width:22px;height:13px;border-radius:7px;background:var(--blue-bright)"></span><span style="width:22px;height:13px;border-radius:7px;background:var(--blue-bright)"></span><span style="width:22px;height:13px;border-radius:7px;background:var(--blue-bright)"></span></div>
  </div>
  <div class="vsep" style="left:122px"></div>
  <div class="vcol" style="left:124px;width:107px;top:52px">
    <svg width="72" height="72" viewBox="0 0 74 74"><circle cx="37" cy="37" r="34" fill="none" stroke="var(--blue-bright)" stroke-width="3"/><path d="M22 37c8-10 22-10 30 0-8 10-22 10-30 0z" fill="var(--blue-bright)"/><circle cx="37" cy="37" r="5" fill="#fff"/><circle cx="37" cy="37" r="2.5" fill="var(--blue-bright)"/></svg>
    <div style="color:var(--link);font-size:12px;line-height:26px"><b style="font-size:22px">10</b> USERS</div>
    <div style="font-size:9.5px;color:#444;line-height:12px">Today Visitor Users</div>
    <div style="font-size:7.5px;color:#777;line-height:11px"><span style="color:#c33">▾</span> 25% this month</div>
  </div>
  <div class="vsep" style="left:231px"></div>
  <div class="vcol" style="left:233px;width:109px;top:52px">
    <svg width="72" height="72" viewBox="0 0 74 74"><circle cx="37" cy="37" r="34" fill="none" stroke="#ddd" stroke-width="3"/><path d="M37 3a34 34 0 1 1-30 50" fill="none" stroke="#444" stroke-width="3"/><circle cx="37" cy="31" r="6" fill="#444"/><path d="M27 47c0-12 20-12 20 0z" fill="#444"/></svg>
    <div style="color:#444;font-size:12px;line-height:26px"><b style="font-size:20px;font-weight:600">632</b>USERS</div>
    <div style="font-size:7.5px;color:#777;line-height:11px;margin-top:2px"><span style="color:#c33">▾</span> 61% this month</div>
  </div>
</section>

<section class="panel rem">
  <div class="tabs">
    <div class="tab on"><svg width="13" height="14" viewBox="0 0 13 14"><path d="M6.5 0C3 0 2 3 2 6v3L0 12h13l-2-3V6c0-3-1-6-4.5-6z" fill="#222"/><circle cx="6.5" cy="13" r="1.5" fill="#222"/></svg>Reminders</div>
    <div class="tab off"><svg width="10" height="9" viewBox="0 0 10 9"><path d="M0 1h10M0 4.5h10M0 8h10" stroke="#444" stroke-width="1.5"/></svg>Activity Feed</div>
  </div>
  <svg class="abs" style="left:14px;top:55px" width="10" height="14" viewBox="0 0 10 14"><path d="M9 1L2 7l7 6" fill="none" stroke="#888" stroke-width="3"/></svg>
  <svg class="abs" style="left:260px;top:55px" width="10" height="14" viewBox="0 0 10 14"><path d="M1 1l7 6-7 6" fill="none" stroke="#888" stroke-width="3"/></svg>
  <div class="month">JUNE 2016</div>
  <table class="cal">
    <tr><th>Su</th><th>Mo</th><th>Tu</th><th>We</th><th>Th</th><th>Fr</th><th>Sa</th></tr>
    <tr><td class="fd">28</td><td class="fd">29</td><td class="fd">30</td><td class="fd">31</td><td>1</td><td>2</td><td class="sel"><span>3</span></td></tr>
    <tr><td>4</td><td>5</td><td class="sel"><span>6</span></td><td>7</td><td>8</td><td>9</td><td>10</td></tr>
    <tr><td>11</td><td>12</td><td>13</td><td>14</td><td>15</td><td>16</td><td>17</td></tr>
    <tr><td>18</td><td class="sel"><span>19</span></td><td>20</td><td>21</td><td>22</td><td>23</td><td>24</td></tr>
    <tr><td>25</td><td>26</td><td>27</td><td>28</td><td>29</td><td>30</td><td class="fd">1</td></tr>
  </table>
  <div class="tip">Evalution point : marketing Coperation Agreement ads ltd</div>
  <svg class="abs" style="left:138px;top:245px" width="10" height="10" viewBox="0 0 10 10"><circle cx="5" cy="5" r="4" fill="none" stroke="#555"/><path d="M5 2.5V5h2" stroke="#555" fill="none"/></svg>
</section>

<section class="panel saved">
  <div class="tabs">
    <div class="tab on" style="width:154px"><svg width="16" height="16" viewBox="0 0 16 16"><circle cx="6.5" cy="6.5" r="5" fill="none" stroke="#222" stroke-width="2"/><path d="M10 10l5 5" stroke="#222" stroke-width="2"/></svg>Saved Searches</div>
    <div class="tab off"><svg width="16" height="12" viewBox="0 0 16 12"><path d="M10 0l6 5-6 5V7C5 7 2 8 0 12 0 6 4 3 10 3z" fill="#333"/></svg>My Latest</div>
  </div>
  <table class="stable">
    <tr><th>Name</th><th>Search Term(s)</th><th>Actions</th></tr>
    <tr><td>Contracts</td><td>*Zen*</td><td class="act">run <i>|</i> edit <i>|</i> delete</td></tr>
    <tr><td>Contracts</td><td>*Zen*</td><td class="act">run <i>|</i> edit <i>|</i> delete</td></tr>
    <tr><td>Contracts</td><td>*Zen*</td><td class="act">run <i>|</i> edit <i>|</i> delete</td></tr>
    <tr><td>Contracts</td><td>*Zen*</td><td class="act">run <i>|</i> edit <i>|</i> delete</td></tr>
    <tr><td>Contracts</td><td>*Zen*</td><td class="act">run <i>|</i> edit <i>|</i> delete</td></tr>
  </table>
</section>

<footer class="foot">
  <span class="c">Copyright © 2016 PactBloom Ltd. All Right Reversed</span>
  <span class="l">Terms of Use &nbsp;&nbsp; | &nbsp;&nbsp; Privacy</span>
</footer>

</body>
</html>
```